Dentist Anesthesiologist
BrookMint Dental
Professional
Rafael Okonkwo, DMD, MPH, MBA
418 North Pine Hollow Road
Suite 207915
Phoenix, Arizona 85093
(877) 555-TOOL (8665)
(480) 555-TOOL (8665)
Dr.Okonkwo@BrookMintDental.example
www.BrookMintDental.example
Please visit my website www.BrookMintDental.example for colors (blue and brown). I am not sure if I want my name to be written as Dr. Rafael Okonkwo or Rafael Okonkwo, DMD, MPH, MBA. In the form above, it didn't ask for the business name - it is BrookMint Dental.
I am okay with textual information or the logo design on the back of the card.
Here is the logo design on my website.
Here is the logo design for my website.

```html
<!DOCTYPE html>
<html lang="en">
<head>
<meta charset="utf-8">
<title>BrookMint Dental – Business Card</title>
<link rel="stylesheet" href="https://fonts.googleapis.com/css2?family=Cinzel:wght@400;600&display=swap">
<style>
  :root {
    --backdrop: #e9e6e1;
    --card: #ffffff;
    --band: #3d86c9;
    --band-edge: #2f74b5;
    --brand-blue: #3a7fc1;
    --brown: #8a6a4a;
    --tab: #b58c63;
    --on-band: #ffffff;
  }
  * { box-sizing: border-box; margin: 0; padding: 0; }
  html, body { width: 1200px; height: 902px; overflow: hidden; }
  body {
    background: var(--backdrop);
    font-family: "Cinzel", serif;
    display: flex; align-items: center; justify-content: center;
  }
  .business-card {
    position: relative;
    width: 1000px; height: 572px;
    background: var(--card);
    box-shadow: 0 12px 30px rgba(0,0,0,.18);
    overflow: hidden;
  }
  .brand {
    position: absolute; top: 60px; left: 0; right: 0;
    text-align: center;
  }
  .brand-name {
    font-size: 64px; font-weight: 600; letter-spacing: 2px;
    color: var(--brand-blue); line-height: 1;
  }
  .tagline {
    margin-top: 28px;
    font-size: 28px; letter-spacing: 3px;
    color: var(--brown);
  }
  .info-band {
    position: absolute; left: 0; right: 0; top: 268px; height: 196px;
    background: linear-gradient(180deg, var(--band) 0%, var(--band-edge) 100%);
    color: var(--on-band);
  }
  .name-tab {
    position: absolute; left: 0; top: 118px; width: 12px; height: 64px;
    background: var(--tab);
  }
  .holder {
    position: absolute; left: 28px; top: 108px;
    font-size: 19px; line-height: 1.35;
  }
  .holder .title { font-size: 15px; margin-top: 4px; letter-spacing: .5px; }
  .contact-list {
    position: absolute; left: 584px; top: 14px;
    list-style: none; font-size: 13.5px; line-height: 22px;
  }
  .contact-list li { display: flex; align-items: center; gap: 10px; white-space: nowrap; }
  .contact-list .icon { width: 12px; height: 12px; flex: none; }
  .contact-list .plain { padding-left: 22px; }
</style>
</head>
<body>
  <div class="business-card">
    <header class="brand">
      <div class="brand-name">BrookMint Dental</div>
      <p class="tagline">THE CALMEST CHAIR IN THE VALLEY</p>
    </header>

    <section class="info-band">
      <span class="name-tab"></span>
      <div class="holder">
        <p>Rafael Okonkwo,<br>DMD, MPH, MBA</p>
        <p class="title">Dentist Anesthesiologist</p>
      </div>

      <ul class="contact-list">
        <li><svg class="icon" viewBox="0 0 12 12"><circle cx="6" cy="6" r="6" fill="#fff"/><circle cx="6" cy="5" r="2" fill="#3d86c9"/></svg>418 North Pine Hollow Road Suite 207915</li>
        <li class="plain">Phoenix, Arizona 85093</li>
        <li><svg class="icon" viewBox="0 0 12 12"><circle cx="6" cy="6" r="6" fill="#fff"/><rect x="4" y="3" width="4" height="6" rx="1" fill="#3d86c9"/></svg>(877) 555-TOOL (8665)</li>
        <li><svg class="icon" viewBox="0 0 12 12"><circle cx="6" cy="6" r="6" fill="#fff"/><rect x="4" y="3" width="4" height="6" rx="1" fill="#3d86c9"/></svg>(480) 555-TOOL (8665)</li>
        <li><svg class="icon" viewBox="0 0 12 12"><circle cx="6" cy="6" r="6" fill="#fff"/><rect x="3" y="4" width="6" height="4" fill="#3d86c9"/></svg>(480) 555-0142</li>
        <li><svg class="icon" viewBox="0 0 12 12"><circle cx="6" cy="6" r="6" fill="#fff"/><path d="M3 4h6v4H3z M3 4l3 2 3-2" fill="none" stroke="#3d86c9" stroke-width="1"/></svg>Dr.Okonkwo@BrookMintDental.example</li>
        <li><svg class="icon" viewBox="0 0 12 12"><circle cx="6" cy="6" r="6" fill="#fff"/><circle cx="6" cy="6" r="3" fill="none" stroke="#3d86c9" stroke-width="1"/></svg>www.BrookMintDental.example</li>
      </ul>
    </section>
  </div>
</body>
</html>
```